Corrowin Sack operates across the US and Australasia providing calico bags to small business through to large enterprise across all verticals. Our bags are the most premium in the market place and our customer service is second to none. Our competitive advantage lays in our competitive pricing, superior quality and outstanding customer service.

Industry/Entity Type

Business

Contact Information for Business Card

Corrowin Sack
Marisol Quenby
Managing Director
marisol@corrowinsack.com
www.corrowinsack.com.au
Mobile:- 0471 896 305
Level 3, 284 Harwick Street
Melbourne Victoria Australia 3000

```html
<!DOCTYPE html>
<html lang="en">
<head>
<meta charset="utf-8">
<title>Corrowin Sack – Business Card</title>
<link rel="stylesheet" href="https://fonts.googleapis.com/css2?family=Open+Sans:wght@400;600&display=swap">
<style>
  :root {
    --stage: #ecebe8;
    --card: #ffffff;
    --green-light: #bfe39a;
    --green-mid: #8cc257;
    --green-dark: #5c9a22;
    --name-green: #6aab2c;
    --ink: #1f1f1f;
    --shadow: rgba(0, 0, 0, 0.12);
  }
  * { box-sizing: border-box; margin: 0; padding: 0; }
  html, body {
    width: 1200px;
    height: 900px;
    overflow: hidden;
    background: var(--stage);
    font-family: "Open Sans", Arial, sans-serif;
    color: var(--ink);
  }
  .canvas { position: relative; width: 1200px; height: 900px; }

  .card {
    position: absolute;
    background: var(--card);
    border-radius: 18px;
    overflow: hidden;
    box-shadow: 0 6px 18px var(--shadow);
  }
  .card--front { left: 78px; top: 35px; width: 588px; height: 362px; }
  .card--back  { left: 390px; top: 506px; width: 564px; height: 350px; }

  .brand-band {
    position: absolute;
    left: 0; top: 27px;
    width: 100%; height: 103px;
    background: linear-gradient(to bottom, var(--green-light), var(--green-mid) 55%, var(--green-dark));
  }
  .brand-seal {
    position: absolute;
    left: 219px; top: -14px;
    width: 150px; height: 150px;
    border-radius: 50%;
    background: var(--card);
  }
  .brand-name {
    position: absolute;
    left: 0; top: 63px;
    width: 100%;
    text-align: center;
    font-weight: 600;
    font-size: 22px;
    color: var(--ink);
    letter-spacing: 0.5px;
  }

  .contact {
    position: absolute;
    left: 0; top: 162px;
    width: 100%;
    text-align: center;
  }
  .contact__name { font-size: 20px; font-weight: 600; color: var(--name-green); line-height: 26px; }
  .contact__role { font-size: 15.5px; line-height: 22px; }
  .contact__lines { margin-top: 19px; list-style: none; }
  .contact__lines li {
    font-size: 16px;
    line-height: 24.5px;
    display: flex;
    justify-content: center;
    align-items: center;
    gap: 4px;
  }
  .contact__lines svg { width: 12px; height: 12px; fill: none; stroke: var(--name-green); stroke-width: 2; }
  .contact__lines svg.solid { fill: var(--name-green); stroke: none; }
  .contact__address { margin-top: 11px; font-size: 16px; line-height: 22px; }

  .map-area {
    position: absolute;
    left: 150px; top: 56px;
    width: 266px; height: 240px;
    border-radius: 42% 48% 40% 44%;
    background: linear-gradient(135deg, var(--green-light), var(--green-mid) 45%, var(--green-dark));
  }
  .back-name {
    position: absolute;
    left: 0; top: 138px;
    width: 100%;
    text-align: center;
    font-weight: 600;
    font-size: 24px;
    color: var(--ink);
    letter-spacing: 0.5px;
  }
</style>
</head>
<body>
<main class="canvas">
  <section class="card card--front">
    <div class="brand-band"></div>
    <div class="brand-seal"></div>
    <div class="brand-name">Corrowin Sack</div>
    <div class="contact">
      <p class="contact__name">Marisol Quenby</p>
      <p class="contact__role">Managing Director</p>
      <ul class="contact__lines">
        <li>
          <svg class="solid" viewBox="0 0 12 12" aria-hidden="true"><path d="M2.5 1l2 2.3-1 1.4a7 7 0 0 0 3.8 3.8l1.4-1 2.3 2-1.2 1.6C5.5 11 1 6.5 0.9 2.2z"/></svg>
          0471 896 305
        </li>
        <li>
          <svg class="solid" viewBox="0 0 12 12" aria-hidden="true"><path d="M0.5 2.5h11v7h-11z M0.5 2.5l5.5 4 5.5-4" /></svg>
          marisol@corrowinsack.com
        </li>
        <li>
          <svg viewBox="0 0 12 12" aria-hidden="true"><path d="M5 7l2-2M4.2 5.5l-1.7 1.7a1.8 1.8 0 0 0 2.5 2.5l1.7-1.7M7.8 6.5l1.7-1.7a1.8 1.8 0 0 0-2.5-2.5L5.3 4"/></svg>
          www.corrowinsack.com.au
        </li>
      </ul>
      <p class="contact__address">Level 3, 284 Harwick Street Melbourne Victoria Australia 3000</p>
    </div>
  </section>

  <section class="card card--back">
    <div class="map-area" role="img" aria-label="Green map of Australia"></div>
    <div class="back-name">Corrowin Sack</div>
  </section>
</main>
</body>
</html>
```